Golden Years Wellness Roadmap: This is my second book. The first was Eldercare Compass

I need a book cover design for: GOLDEN YEARS WELLNESS ROADMAP: A NO-EXPENSE METHOD FOR FINISHING YOUR LATER-LIFE MOSAIC WITH POOLED KVB CARE SCHEMES by Derek Holloway Neil Osgrove & Martin Quarles. This book is designed for business owners, CEO's, CFO's and Human Resources. The cover needs to be professional and focused on business. The purpose of this book is to educate business owners and their management about a zero cost retiree health plan. This is a first of it's kind solution that every business needs to learn about.

Target Market(s)

Business owners, CEO's, CFO's and Human Resources

Requirements
Nice to have
• I want the design to be clean and professional since it is focused on business executives

```html
<!DOCTYPE html>
<html lang="en">
<head>
<meta charset="utf-8">
<title>Golden Years Wellness Roadmap – Book Cover</title>
<link rel="stylesheet" href="https://fonts.googleapis.com/css2?family=Jost:wght@400;500;600&display=swap">
<style>
  :root {
    --stage: #6f6f6f;
    --paper: #ffffff;
    --paper-shade: #f1f2f5;
    --navy: #0b1870;
    --band: #0a176a;
    --royal: #1f3fae;
    --sky: #3a74d6;
    --art-deep: #0d2a9a;
    --art-mid: #2a5ed8;
    --art-light: #8fc3f2;
  }
  * { box-sizing: border-box; margin: 0; padding: 0; }
  html, body {
    width: 1200px; height: 663px; overflow: hidden;
    background: var(--stage);
  }
  .stage {
    width: 1200px; height: 663px;
    display: flex; align-items: center; justify-content: center;
  }
  .cover {
    width: 410px; height: 600px;
    display: flex; flex-direction: column;
    background: linear-gradient(100deg, var(--paper) 0%, var(--paper) 55%, var(--paper-shade) 100%);
    font-family: "Jost", "Futura", sans-serif;
    overflow: hidden;
  }
  .cover-art {
    height: 280px;
    background:
      radial-gradient(ellipse 28% 38% at 56% 48%, var(--art-light) 0%, rgba(143,195,242,0) 100%),
      radial-gradient(circle at 58% 20%, #cfe6ff 0%, rgba(207,230,255,0) 18%),
      linear-gradient(160deg, var(--art-deep) 0%, var(--art-mid) 55%, var(--art-deep) 100%);
  }
  .title-block {
    flex: 1;
    display: flex; flex-direction: column; align-items: center;
    padding-top: 22px;
    text-align: center;
  }
  .book-title {
    color: var(--navy);
    font-weight: 500;
    font-size: 41px;
    line-height: 49px;
    letter-spacing: 0.12em;
    text-transform: uppercase;
    margin-right: -0.12em;
  }
  .book-subtitle {
    margin-top: 14px;
    font-weight: 500;
    font-size: 12.5px;
    line-height: 18px;
    letter-spacing: 0.06em;
    color: var(--royal);
    text-transform: uppercase;
  }
  .book-subtitle .lead { color: var(--sky); }
  .author-band {
    height: 71px;
    background: var(--band);
    display: flex; align-items: center; justify-content: center;
  }
  .authors {
    color: var(--paper);
    font-weight: 500;
    font-size: 12px;
    letter-spacing: 0.07em;
    text-transform: uppercase;
  }
</style>
</head>
<body>
  <main class="stage">
    <article class="cover">
      <div class="cover-art" role="img" aria-label="Cover artwork: upward view between blue glass skyscrapers framing a cross-shaped opening to a sunlit cloudy sky, with a wireframe stethoscope in the lower left"></div>
      <section class="title-block">
        <h1 class="book-title">Golden Years<br>Wellness<br>Roadmap</h1>
        <p class="book-subtitle">
          <span class="lead">A No-Expense Method For</span><br>
          Finishing Your Later-Life Mosaic<br>
          With Pooled KVB Care Schemes
        </p>
      </section>
      <footer class="author-band">
        <p class="authors">Derek Holloway, Neil Osgrove &amp; Martin Quarles</p>
      </footer>
    </article>
  </main>
</body>
</html>
```